Financial management business is partnering with chef for a cooking demo and financial workshop j...

We need an promotional invitation/postcard to our event called "Kitchen Table Talks: Cooking Smart All Year Long."

Target Market(s)

55+, seniors

Font styles to use
Serif

Requirements
Must have
• EDDM formatting 6"x9"

```html
<!DOCTYPE html>
<html lang="en">
<head>
<meta charset="UTF-8">
<title>Kitchen Table Talks – Event Postcard</title>
<link rel="stylesheet" href="https://fonts.googleapis.com/css2?family=Archivo:wght@400;800;900&family=Roboto:wght@400;500&family=Montserrat:wght@400;500&display=swap">
<style>
  :root{
    --backdrop:#c3cfbc;
    --paper:#ffffff;
    --band-green:rgba(54,101,28,.93);
    --panel-green:#436b2c;
    --heading-green:#3f6b24;
    --ink:#3a3a3a;
    --ink-soft:#4a4a4a;
    --rule:#5b5b5b;
    --brand-navy:#2b3aa0;
  }
  *{box-sizing:border-box;margin:0;padding:0}
  html,body{width:1200px;height:1200px;overflow:hidden}
  body{background:var(--backdrop);position:relative;font-family:'Roboto',sans-serif;color:var(--ink)}

  .postcard{position:absolute;left:266px;width:668px;height:476px;background:var(--paper)}
  .postcard--front{top:82px}
  .postcard--back{top:642px}

  /* FRONT */
  .hero-photo{position:absolute;left:11px;top:13px;width:646px;height:419px;
    background:linear-gradient(160deg,#3f5a30 0%,#6f8a55 35%,#c9c4b4 55%,#7e8f5f 75%,#3c5528 100%)}
  .title-band{position:absolute;left:11px;top:304px;width:646px;height:128px;background:var(--band-green);color:#fff;text-align:center}
  .event-title{font-family:'Archivo',sans-serif;line-height:1}
  .event-title__main{display:block;font-weight:900;font-size:27px;letter-spacing:.5px;text-transform:uppercase;padding-top:16px}
  .event-title__sub{display:block;font-weight:400;font-size:28px;text-transform:uppercase;margin-top:8px}
  .event-details{position:absolute;top:89px;left:0;width:100%;display:flex;justify-content:center;gap:17px}
  .detail{display:flex;height:22px;border:1px solid #fff;font-family:'Montserrat',sans-serif;font-size:16px;line-height:20px}
  .detail__label{background:#fff;color:#222;padding:0 6px}
  .detail__value{padding:0 6px;color:#fff}
  .sponsor{position:absolute;top:443px;left:0;width:100%;text-align:center;font-family:'Montserrat',sans-serif;font-size:13px;color:var(--ink)}
  .sponsor__brand{margin-left:8px;color:var(--brand-navy);font-weight:500;letter-spacing:1px;text-transform:uppercase;font-size:12px}

  /* BACK */
  .kitchen-photo{position:absolute;left:11px;top:0;width:262px;height:266px;
    background:linear-gradient(135deg,#e9e6e1 0%,#d8d2cb 40%,#2e2e30 60%,#cfd3db 100%)}
  .partner-mark{position:absolute;left:283px;top:30px;width:375px;text-align:center}
  .partner-mark__dot{display:inline-block;width:30px;height:30px;border-radius:50%;background:#7a2233}
  .partner-mark__name{display:block;margin-top:6px;font-family:'Archivo',sans-serif;font-weight:800;font-size:14px;color:#222;letter-spacing:.3px;text-transform:uppercase}
  .intro-panel{position:absolute;left:283px;top:94px;width:375px;height:172px;background:var(--panel-green);color:#fff;padding:50px 16px 0}
  .intro-panel__title{font-family:'Archivo',sans-serif;font-size:13px;line-height:16px;text-transform:uppercase}
  .intro-panel__title b{font-weight:900;display:block}
  .intro-panel__title span{font-weight:400;display:block}
  .intro-panel__text{margin-top:10px;font-size:9px;line-height:11.2px;text-align:justify}

  .bio-photo{position:absolute;top:289px;width:124px;height:142px}
  .bio-photo--planner{left:19px;background:linear-gradient(180deg,#8b8f86 0%,#c59f88 45%,#1f2433 100%)}
  .bio-photo--chef{left:351px;background:linear-gradient(180deg,#6b6a66 0%,#b58b72 45%,#f1f1ef 100%)}
  .bio{position:absolute;top:293px}
  .bio--planner{left:166px;width:161px}
  .bio--chef{left:492px;width:154px}
  .bio__heading{font-family:'Archivo',sans-serif;font-weight:400;font-size:12.5px;line-height:14px;color:var(--heading-green);text-transform:uppercase}
  .bio__text{margin-top:7px;font-size:9px;line-height:11.1px;color:var(--ink-soft)}
  .bio--planner .bio__text{text-align:justify}
  .bio--chef .bio__text{margin-top:6px}
  .bottom-rule{position:absolute;left:11px;top:461px;width:646px;height:5px;background:var(--rule)}
</style>
</head>
<body>

<section class="postcard postcard--front" aria-label="Postcard front">
  <div class="hero-photo" role="img" aria-label="Photo of a smiling couple in a vegetable garden holding a basket of fresh produce"></div>
  <div class="title-band">
    <h1 class="event-title">
      <span class="event-title__main">Kitchen Table Talks:</span>
      <span class="event-title__sub">Cooking Smart All Year Long</span>
    </h1>
    <div class="event-details">
      <div class="detail"><span class="detail__label">When</span><span class="detail__value">Tuesday, July 23rd at 12:30 p.m.</span></div>
      <div class="detail"><span class="detail__label">Where</span><span class="detail__value">Linden Hall&nbsp;&nbsp;&nbsp;</span></div>
    </div>
  </div>
  <p class="sponsor">Sponsored by Hollis Financial <span class="sponsor__brand">Hollis Advisors</span></p>
</section>

<section class="postcard postcard--back" aria-label="Postcard back">
  <div class="kitchen-photo" role="img" aria-label="Photo of a chef preparing vegetables in a home kitchen while a senior woman watches"></div>

  <div class="partner-mark">
    <span class="partner-mark__dot"></span>
    <span class="partner-mark__name">Supper Circle</span>
  </div>

  <div class="intro-panel">
    <h2 class="intro-panel__title"><b>Kitchen Table Talks:</b><span>Cooking Smart All Year Long</span></h2>
    <p class="intro-panel__text">Learn from Chef Dean Porter how to build a menu full of flavor, nutrition, and seasonal ingredients with ease. Followed by a financial workshop where Walt Hollis, Certified Financial Planner, will have some fresh investment ideas to go along with your farm-to-table meal. Walt encourages any questions you may have.</p>
  </div>

  <div class="bio-photo bio-photo--planner" role="img" aria-label="Portrait photo of financial planner Walt Hollis"></div>
  <div class="bio bio--planner">
    <h3 class="bio__heading">A Certified Financial Planner You Can Trust.</h3>
    <p class="bio__text">Walt Hollis is a Certified Financial Planner, specializing in asset management of IRA, retirement, investment, and trust accounts. Hollis Advisors, LLC is an independent Registered Investment Advisor with low cost, commission free business model. Concierge level service is provided to Maple Ridge residents.</p>
  </div>

  <div class="bio-photo bio-photo--chef" role="img" aria-label="Portrait photo of Chef Dean Porter in chef whites"></div>
  <div class="bio bio--chef">
    <h3 class="bio__heading">Chef Dean Porter</h3>
    <p class="bio__text">Chef Dean Porter is a formally trained chef with over 15 years of experience. He started Supper Circle Raleigh, a meal service that connects seniors with licensed, professional chefs who prepare high-quality, affordable, and nutritious meals in the home. Dean is so pleased to have found an opportunity to share his passion for food and connect with local Seniors.</p>
  </div>

  <div class="bottom-rule"></div>
</section>

</body>
</html>
```